11th Annual VarTQ Forum Flyer - Save the Date

We need a flyer for our annual Forum that will be creative with the theme of the Forum while highlighting our conference Title and Topics. Flyer should allow for a header that can be used consistently across conference communication. This is our 11th Annual Forum, which will take place outside of Houston, Texas at El Mirador Resort and Spa.

Target Market(s)

Architects, engineers, contractors, universities, building project Owners

Industry/Entity Type

Construction

Font styles to use
Sans Serif

Colors

Designer to choose colors to be used in the design.

Requirements
Must have
• Title, date, location, key topics (title only), logo. See attached for breakdown of information.
Nice to have
• Creativity with the theme of the Forum, ability to slice flyer so that a portion can be used for a header in other conference documents.
• Mention of Closing Keynote, Dale Porter
Should not have
• Please don't use the topic descriptions in the Flyer. Just the main titles of the topics is necessary.
• Should not be too word, but eye-catching with graphics and main

```html
<!DOCTYPE html>
<html lang="en">
<head>
<meta charset="utf-8">
<title>2019 VarTQ Forum Flyer</title>
<link href="https://fonts.googleapis.com/css2?family=Open+Sans:wght@400;600;700;800&display=swap" rel="stylesheet">
<style>
  :root {
    --navy: #223e78;
    --navy-deep: #1a2f5e;
    --royal: #2f56a6;
    --sky: #5aa8e6;
    --white: #ffffff;
    --ink: #1f2a44;
    --page: #ececec;
    --photo-a: #5d6a5c;
    --photo-b: #a4ab9c;
    --photo-c: #c9cbc1;
  }
  * { box-sizing: border-box; margin: 0; padding: 0; }
  html, body { width: 1200px; height: 984px; overflow: hidden; background: var(--page); }
  body { font-family: "Open Sans", Arial, sans-serif; position: relative; }

  .flyer {
    position: absolute; left: 237px; top: 22px;
    width: 726px; height: 940px;
    background: var(--white);
    overflow: hidden;
    box-shadow: 0 6px 24px rgba(0,0,0,.18);
  }
  .flyer-shapes { position: absolute; inset: 0; }

  .city-photo {
    position: absolute; left: 0; top: 60px; width: 726px; height: 500px;
    background: linear-gradient(160deg, var(--photo-c) 0%, var(--photo-b) 35%, var(--photo-a) 75%, #3f4c45 100%);
    clip-path: polygon(70px 0, 726px 0, 726px 450px, 0 500px, 0 120px);
  }

  .header-label {
    position: absolute; left: 28px; top: 18px;
    color: var(--white); font-weight: 700; font-size: 20px; letter-spacing: .3px;
  }

  .brand {
    position: absolute; right: 14px; top: 6px;
    width: 220px; height: 96px;
    background: var(--white);
    border: 4px solid var(--sky);
    border-radius: 48px;
    display: flex; align-items: center; justify-content: center; gap: 10px;
  }
  .brand-dot { width: 28px; height: 28px; border-radius: 50%; background: var(--navy); }
  .brand-name { color: var(--navy); font-weight: 700; font-size: 30px; }

  .forum-title {
    position: absolute; right: 80px; top: 544px;
    color: var(--white); font-weight: 800; font-size: 30px; line-height: 1.15;
    text-align: center;
  }
  .forum-when {
    position: absolute; right: 80px; top: 622px;
    color: var(--white); font-size: 13px; font-weight: 600; text-align: right;
  }

  .topic-list {
    position: absolute; left: 150px; top: 672px; list-style: none;
  }
  .topic-list li {
    display: flex; align-items: center; gap: 14px;
    color: var(--white); font-size: 19px; font-weight: 600; margin-bottom: 12px;
  }
  .topic-icon { width: 26px; height: 16px; flex: none; }

  .schedule {
    position: absolute; top: 808px; left: 125px; right: 30px;
    display: flex; gap: 28px;
    font-size: 8px; line-height: 1.35; color: var(--ink);
  }
  .schedule-col { flex: 1; }
  .schedule p { margin-bottom: 5px; }
  .schedule strong { font-weight: 700; }

  .site-url {
    position: absolute; right: 120px; top: 876px;
    font-size: 14px; color: var(--navy); font-weight: 600;
  }

  .contact-band {
    position: absolute; left: 0; right: 0; bottom: 0; height: 38px;
    background: var(--royal);
    color: var(--white); font-size: 16px;
    display: flex; align-items: center; padding-left: 40px;
  }
</style>
</head>
<body>
  <article class="flyer">
    <div class="city-photo" role="img" aria-label="Aerial photograph of a city business district with glass office towers beside a river"></div>

    <svg class="flyer-shapes" width="726" height="940" viewBox="0 0 726 940" aria-hidden="true">
      <defs>
        <linearGradient id="bandGrad" x1="0" x2="1">
          <stop offset="0" stop-color="#3f63a8"/>
          <stop offset="1" stop-color="#243f7c"/>
        </linearGradient>
      </defs>
      <rect x="0" y="0" width="726" height="60" fill="url(#bandGrad)"/>
      <polygon points="0,0 90,0 0,110" fill="#6f8fc6" opacity=".55"/>
      <polygon points="0,60 70,60 0,180" fill="#2f56a6"/>
      <polygon points="0,180 70,60 90,60 0,220" fill="#5aa8e6" opacity=".7"/>
      <polygon points="0,560 300,530 726,510 726,800 0,800" fill="#223e78"/>
      <polygon points="560,520 726,510 726,800 660,800" fill="#1a2f5e"/>
      <polygon points="700,600 726,600 726,790 660,790" fill="#ffffff"/>
      <polygon points="686,600 700,600 660,790 630,790" fill="#223e78"/>
      <polygon points="622,660 662,660 650,770 610,770" fill="#5aa8e6"/>
      <polygon points="0,560 300,530 70,940 0,940" fill="#2f56a6"/>
      <polygon points="250,535 300,530 70,940 20,940" fill="#5aa8e6"/>
      <polygon points="110,800 726,800 726,902 55,902" fill="#ffffff"/>
    </svg>

    <div class="header-label">2019 VarTQ Forum</div>

    <div class="brand">
      <span class="brand-dot"></span>
      <span class="brand-name">I-VarTQ</span>
    </div>

    <h1 class="forum-title">The Three-Legged Stool<br>Balanced or Broken?</h1>
    <p class="forum-when">Thursday &amp; Friday, 2019 · El Mirador Resort and Spa, near Houston, Texas</p>

    <ul class="topic-list">
      <li><svg class="topic-icon" viewBox="0 0 26 16"><path d="M2 8 L9 14 L24 2" fill="none" stroke="#fff" stroke-width="2.2"/></svg>The Right Contract management</li>
      <li><svg class="topic-icon" viewBox="0 0 26 16"><path d="M2 8 L9 14 L24 2" fill="none" stroke="#fff" stroke-width="2.2"/></svg>The Right Culture</li>
      <li><svg class="topic-icon" viewBox="0 0 26 16"><path d="M2 8 L9 14 L24 2" fill="none" stroke="#fff" stroke-width="2.2"/></svg>The Right Subcontractors</li>
    </ul>

    <section class="schedule">
      <div class="schedule-col">
        <p><strong>Thursday : Opening Keynote</strong> – "The Three-Legged Stool Balanced or Broken?" Through a panel discussion with an Owner, contractor, and designer, this session sets the context for our Forum theme. What works, and what may be missing?</p>
        <p><strong>Lunch Presentation</strong> – Case study on team leadership in capital projects.</p>
      </div>
      <div class="schedule-col">
        <p><strong>Friday : Closing Keynote, Dale Porter</strong>, author of "The Well Office Shift" and "The Building Reset."</p>
        <p><strong>Final Wrap-Up</strong> – Final wrap-up, discussion, and door prizes.</p>
      </div>
    </section>

    <div class="site-url">www.i-vartq.com</div>

    <footer class="contact-band">Contact Us : Office: (512) 555-0147</footer>
  </article>
</body>
</html>
```